" Trabalhamos visitando nossos clientes no porta a portas, clientes esses com escolas, colégios e creches particulares e prefeituras. Fora a venda particular, participamos de licitações em prefeituras. "

```html
<!DOCTYPE html>
<html lang="pt-BR">
<head>
<meta charset="utf-8">
<title>Assinatura de e-mail – Nova Prima</title>
<link href="https://fonts.googleapis.com/css2?family=Montserrat:wght@500;700&display=swap" rel="stylesheet">
<style>
  :root {
    --page-bg: #f2f2f2;
    --card-bg: #ffffff;
    --gold: #b38b3a;
    --gold-dark: #8a6424;
    --gold-light: #e6c877;
    --ink: #1e1e1e;
  }
  * { margin: 0; padding: 0; box-sizing: border-box; }
  html, body {
    width: 1200px; height: 1200px; overflow: hidden;
    background: var(--page-bg);
    font-family: "Montserrat", sans-serif;
  }
  .signature {
    position: absolute;
    left: 50px; top: 398px;
    width: 1100px; height: 405px;
    background: var(--card-bg);
  }
  .brand {
    position: absolute;
    left: 0; top: 0;
    width: 560px; height: 100%;
    display: flex; align-items: center; justify-content: center;
    gap: 22px;
  }
  .brand-mark {
    width: 34px; height: 34px;
    background: var(--gold);
  }
  .brand-name {
    font-family: "Montserrat", sans-serif;
    font-weight: 500;
    font-size: 50px;
    letter-spacing: 4px;
    color: var(--gold);
    text-transform: uppercase;
  }
  .contacts {
    position: absolute;
    left: 572px; top: 116px;
    list-style: none;
  }
  .contact {
    display: flex; align-items: center;
    height: 48px;
    margin-bottom: 18px;
  }
  .contact-icon {
    width: 48px; height: 48px;
    border-radius: 4px;
    background: linear-gradient(135deg, var(--gold-dark), var(--gold-light) 55%, var(--gold) 100%);
    display: flex; align-items: center; justify-content: center;
    margin-right: 18px;
  }
  .contact-icon svg { width: 28px; height: 28px; }
  .contact-text {
    font-weight: 700;
    font-size: 23px;
    letter-spacing: 1px;
    color: var(--ink);
  }
</style>
</head>
<body>
  <section class="signature">
    <div class="brand">
      <span class="brand-mark"></span>
      <span class="brand-name">Nova Prima</span>
    </div>
    <ul class="contacts">
      <li class="contact">
        <span class="contact-icon">
          <svg viewBox="0 0 24 24" fill="none" stroke="#fff" stroke-width="1.8" stroke-linecap="round" stroke-linejoin="round"><path d="M5 3h4l2 5-2.5 1.5a11 11 0 0 0 6 6L16 13l5 2v4a2 2 0 0 1-2 2A16 16 0 0 1 3 5a2 2 0 0 1 2-2z"/></svg>
        </span>
        <span class="contact-text">(85) 90000-1234 | 90000-5678</span>
      </li>
      <li class="contact">
        <span class="contact-icon">
          <svg viewBox="0 0 24 24" fill="none" stroke="#fff" stroke-width="1.8" stroke-linejoin="round"><rect x="3" y="5" width="18" height="14" rx="2"/><path d="M3 7l9 6 9-6"/></svg>
        </span>
        <span class="contact-text">NOVAPRIMA@EXEMPLO.COM</span>
      </li>
      <li class="contact">
        <span class="contact-icon">
          <svg viewBox="0 0 24 24" fill="none" stroke="#fff" stroke-width="1.6"><circle cx="12" cy="12" r="9"/><ellipse cx="12" cy="12" rx="4" ry="9"/><path d="M3 12h18M5 7h14M5 17h14"/></svg>
        </span>
        <span class="contact-text">NOVAPRIMA.COM.BR</span>
      </li>
    </ul>
  </section>
</body>
</html>
```